Stationery Design Project for Bramble Co

Hi All,

We need you to design stationary for a new online financial services business. We have already got the logo designed and it is attached. If you would like it in any other formats please let me know. If you could also if possible, match the fonts in your design to that on the logo’s provided.

What we need:
- Business Card
- A4 Letter head
- A4 Folders
- PPT template (Title page and regular page)

And what ever else you want to throw in.

We are in the process of getting the web site designed, however below is a list of websites which we like which will give you an understanding of the style that we are going for.

- plimo.com
- brambleroute.com
- tallowquay.com
- pelkwintry.com

I look forward to your seeing your design.

Industry/Entity Type

Financial

Requirements
Must have
• Outputs:
- Documents ready to print
- Generic editable information
- Pdf copies of the documents
- Word version of letterhead

```html
<!DOCTYPE html>
<html lang="en">
<head>
<meta charset="utf-8">
<title>Bramble Co — Stationery Suite</title>
<link rel="stylesheet" href="https://fonts.googleapis.com/css2?family=Nunito:wght@600&family=Open+Sans:wght@400;700&display=swap">
<style>
  :root{
    --blue:#1a82b5;
    --orange:#f7941d;
    --ink:#2b2b3b;
    --paper:#ffffff;
    --stage:#e8e5e1;
    --muted:#555a63;
  }
  *{box-sizing:border-box;margin:0;padding:0}
  html,body{width:1200px;height:900px;overflow:hidden}
  body{background:var(--stage);font-family:"Open Sans",Arial,sans-serif;color:var(--ink);position:relative}
  .sheet{position:absolute;background:var(--paper);box-shadow:0 2px 6px rgba(0,0,0,.18);overflow:hidden}
  .mark{display:flex;align-items:center;gap:8px;position:absolute}
  .mark-dot{width:22px;height:22px;border-radius:50%;background:var(--orange);flex:none}
  .mark-name{font-family:"Nunito",Arial,sans-serif;font-weight:600;font-size:20px;color:var(--ink);white-space:nowrap}
  .mark.on-blue .mark-name{color:#fff}
  .mark.small .mark-dot{width:17px;height:17px}
  .mark.small .mark-name{font-size:15px}
  .seal{position:absolute;width:32px;height:32px;border-radius:50%;background:var(--orange);border:4px solid #fff;box-shadow:0 0 0 1px rgba(0,0,0,.05)}
  .band{position:absolute;left:0;right:0;background:var(--blue)}
  .rule{position:absolute;left:0;right:0;height:2px;background:var(--orange)}
  .url{position:absolute;left:0;right:0;text-align:center;font-size:6px;color:#fff;letter-spacing:.3px}
  .contact{position:absolute;font-size:6px;line-height:1.45;color:var(--muted);white-space:nowrap}
  .contact.tiny{font-size:5px;line-height:1.15}
  .person{position:absolute;font-size:8px;color:var(--ink)}
  .person small{display:block;font-size:5px;color:var(--muted)}
  .divider{position:absolute;width:1px;background:#777}

  /* business cards */
  .card{left:22px;width:233px;height:132px}
  .card-front{top:60px}
  .card-blue{top:203px;background:var(--blue)}
  .card-back{top:345px}
  .card-back-logo{top:487px}
  .card .band{bottom:0;height:20px}
  .card .rule{bottom:22px}

  /* letterhead */
  .letterhead{left:268px;top:60px;width:388px;height:548px}

  /* presentation */
  .slide{left:669px;top:65px;width:424px;height:318px}
  .slide-title{position:absolute;left:19px;top:154px;font-weight:700;font-size:22px;color:#111}
  .slide-photo{position:absolute;width:92px;height:60px}

  /* envelope */
  .envelope{left:286px;top:623px;width:357px;height:218px}

  /* folder */
  .folder-left{left:670px;top:402px;width:247px;height:330px}
  .folder-right{left:917px;top:402px;width:247px;height:330px}
</style>
</head>
<body>

<section class="sheet card card-front" aria-label="Business card front">
  <div class="mark" style="left:32px;top:56px"><span class="mark-dot"></span><span class="mark-name">Bramble Co</span></div>
</section>

<section class="sheet card card-blue" aria-label="Business card front, blue">
  <div class="mark on-blue" style="left:32px;top:55px"><span class="mark-dot"></span><span class="mark-name">Bramble Co</span></div>
</section>

<section class="sheet card card-back" aria-label="Business card back">
  <p class="person" style="left:10px;top:46px">Mara Ellison<small>Founder/CEO</small></p>
  <span class="divider" style="left:97px;top:33px;height:40px"></span>
  <p class="contact" style="left:116px;top:30px">88 Linden Row<br>Austin | 78701<br>☎ 5550142837<br>☎ 5550198264<br>✉ hello@bramblemail.com<br>● www.bramblecofinance.com</p>
  <div class="rule"></div><div class="band"></div>
  <span class="seal" style="left:175px;top:88px"></span>
</section>

<section class="sheet card card-back-logo" aria-label="Business card back with wordmark">
  <div class="mark small" style="left:52px;top:12px"><span class="mark-dot"></span><span class="mark-name">Bramble Co</span></div>
  <p class="person" style="left:10px;top:54px">Mara Ellison<small>Founder/CEO</small></p>
  <span class="divider" style="left:97px;top:42px;height:40px"></span>
  <p class="contact" style="left:116px;top:38px">88 Linden Row<br>Austin | 78701<br>☎ 5550142837<br>☎ 5550198264<br>✉ hello@bramblemail.com<br>● www.bramblecofinance.com</p>
  <div class="rule"></div><div class="band"></div>
  <span class="seal" style="left:175px;top:88px"></span>
</section>

<section class="sheet letterhead" aria-label="Letterhead">
  <div class="band" style="top:0;height:32px"></div>
  <div class="mark small on-blue" style="left:122px;top:7px"><span class="mark-dot"></span><span class="mark-name">Bramble Co</span></div>
  <div class="rule" style="top:524px"></div>
  <div class="band" style="bottom:0;height:21px"></div>
  <p class="url" style="bottom:6px">● www.bramblecofinance.com</p>
  <span class="seal" style="left:328px;top:502px"></span>
</section>

<section class="sheet slide" aria-label="Presentation title slide">
  <svg width="424" height="50" style="position:absolute;left:0;top:0" aria-hidden="true">
    <path d="M0 32 C60 22 130 18 210 0" fill="none" stroke="var(--orange)" stroke-width="2.5"/>
    <path d="M0 38 C70 28 140 22 212 2" fill="none" stroke="var(--blue)" stroke-width="3"/>
  </svg>
  <h1 class="slide-title">Presention title</h1>
  <div class="slide-photo" role="img" aria-label="Photo of colourful bokeh lights" style="left:225px;top:15px;background:radial-gradient(circle at 40% 45%,#6a8a7c,#1d2a2e 70%)"></div>
  <div class="slide-photo" role="img" aria-label="Photo of a dark abstract light sculpture" style="left:317px;top:75px;background:radial-gradient(circle at 45% 40%,#5c6068,#0b0b0d 70%)"></div>
  <div class="slide-photo" role="img" aria-label="Photo of white light streaks on black" style="left:225px;top:136px;height:62px;background:radial-gradient(circle at 50% 55%,#c9c9c4,#111 60%)"></div>
  <div class="slide-photo" role="img" aria-label="Photo of a vivid orange and red painting" style="left:317px;top:197px;background:linear-gradient(120deg,#e05a1c,#9e2b16 55%,#e28b2c)"></div>
  <div class="band" style="bottom:0;height:20px"></div>
  <p class="url" style="bottom:6px">● www.bramblecofinance.com</p>
  <span class="seal" style="left:366px;top:272px"></span>
</section>

<section class="sheet envelope" aria-label="Envelope">
  <div class="band" style="top:0;height:40px"></div>
  <span class="seal" style="left:161px;top:3px"></span>
  <div class="mark small" style="left:11px;top:53px"><span class="mark-dot"></span><span class="mark-name">Bramble Co</span></div>
  <p class="contact tiny" style="left:8px;top:162px">88 Linden Row<br>Austin | 78701<br>✉ hello@bramblemail.com<br>● www.bramblecofinance.com</p>
  <div class="rule" style="top:194px"></div>
  <div class="band" style="bottom:0;height:21px"></div>
  <span class="seal" style="left:299px;top:172px"></span>
</section>

<section class="sheet folder-left" aria-label="Folder back cover">
  <div class="rule" style="top:286px"></div>
  <div class="band" style="bottom:0;height:42px"></div>
  <p class="contact tiny" style="left:8px;top:291px;color:#fff">88 Linden Row<br>Austin | 78701<br>☎ 5550142837<br>☎ 5550198264<br>✉ hello@bramblemail.com<br>● www.bramblecofinance.com</p>
  <span class="seal" style="left:195px;top:294px"></span>
</section>

<section class="sheet folder-right" aria-label="Folder front cover">
  <div class="band" style="top:0;height:40px"></div>
  <div class="mark small on-blue" style="left:46px;top:10px"><span class="mark-dot"></span><span class="mark-name">Bramble Co</span></div>
  <div class="rule" style="top:308px"></div>
  <p class="url" style="top:315px;color:var(--ink)">● www.bramblecofinance.com</p>
  <span class="seal" style="left:190px;top:285px"></span>
</section>

<svg width="1200" height="900" style="position:absolute;left:0;top:0;pointer-events:none" aria-hidden="true">
  <path d="M918 734 L1162 734 L1162 838 L926 838 Z" fill="var(--blue)" stroke="#fff" stroke-width="1"/>
  <path d="M1164 622 L1178 624 L1180 700 L1166 734 L1164 734 Z" fill="var(--blue)" stroke="#fff" stroke-width="1"/>
</svg>

</body>
</html>
```